Website Design - clean, cutting-edge, impressive and lively

We need to upgrade the design (content will stay the same) of our current site: https://brightpage-web.co.il/index.php?lang=en
1. We need a design that is more sophisticated, cutting-edge, and impressive.
2. At the same time, it is important for the site to remain clean and clear (to create feeling of transparency and trust with client).
3. Lastly, the site design must be in line with our logo in its projection of a service that is friendly and sites that are lively.
Target Market(s)
medium-sized businesses, such as VCs, Pharma, and other companies that need brochure-like sites (not ecommerce and not sites dependent on active online marketing).
Industry/Entity Type
Website
Number of Pages Required
2 page
Look and feel
Each slider illustrates characteristics of the customer's brand and the style your logo design should communicate.

```html
<!DOCTYPE html>
<html lang="en">
<head>
<meta charset="utf-8">
<title>BrightPage – We Create the Web</title>
<link href="https://fonts.googleapis.com/css2?family=Poppins:wght@300;400;500;600;700;800&display=swap" rel="stylesheet">
<style>
:root{
  --orange:#f15a29;
  --green:#8cc63f;
  --purple:#7352ad;
  --yellow:#fcc30b;
  --ink:#3a3a3a;
  --muted:#666;
  --ghost:#f4f1f1;
  --white:#fff;
}
*{margin:0;padding:0;box-sizing:border-box}
html,body{width:708px;height:1200px;overflow:hidden;background:var(--white);font-family:'Poppins',sans-serif;color:var(--ink)}
.page{position:relative;width:708px;height:1200px;overflow:hidden}
.abs{position:absolute}

.topbar{left:0;top:0;width:708px;height:22px;background:var(--orange)}
.contact{left:94px;top:0;height:22px;display:flex;align-items:center;gap:12px;color:var(--white);font-size:6px}
.contact span{display:flex;align-items:center;gap:3px}
.tabs{right:0;top:0;width:240px;height:22px}
.tab-label{font-size:5.5px;color:var(--white);top:0;line-height:22px}

.header{left:0;top:22px;width:708px;height:49px;background:var(--white);border-bottom:1px solid #e8e0dc}
.brand{left:99px;top:22px;height:49px;display:flex;align-items:center;gap:5px;font-size:17px;font-weight:500;color:#555;letter-spacing:-.3px;line-height:1}
.brand i{display:block;width:9px;height:9px;background:var(--orange)}
.nav{right:99px;top:44px;display:flex;gap:12px;font-size:5.8px;letter-spacing:.3px;color:#444}
.nav .active{color:#999}

.hero{left:0;top:71px;width:708px;height:368px;background:
  linear-gradient(rgba(40,30,40,.45),rgba(40,30,40,.45)),
  linear-gradient(120deg,#6f7a85 0%,#8d8f95 30%,#7a5a48 55%,#a07f68 75%,#c8b7a8 100%)}
.hero-title{left:0;top:183px;width:708px;text-align:center;color:var(--white);font-weight:800;font-size:41px;line-height:44px;letter-spacing:2px}
.hero-sub{left:0;top:285px;width:708px;text-align:center;color:var(--white);font-size:9.5px;font-weight:500;letter-spacing:.3px}
.hero-btn{left:290px;top:329px;width:126px;height:24px;background:var(--yellow);color:#6b4a10;font-size:7px;font-weight:600;letter-spacing:.6px;display:flex;align-items:center;justify-content:center}

.ghost{left:456px;top:498px;color:var(--ghost);font-weight:800;font-size:56px;line-height:58px;letter-spacing:-1px;text-align:center;width:230px}
.intro-shape{left:0;top:409px}
.intro-title{left:104px;top:428px;width:280px;color:var(--white);font-size:16.8px;font-weight:600;line-height:22px}
.intro-text{left:104px;top:549px;width:290px;color:var(--white);font-size:9.4px;font-weight:300;line-height:14.8px}
.intro-btn{left:104px;top:629px;width:155px;height:33px;background:var(--white);color:var(--purple);font-size:11px;font-weight:500;letter-spacing:.5px;display:flex;align-items:center;justify-content:center}

.projects-title{left:0;top:726px;width:708px;text-align:center;color:var(--orange);font-size:28px;font-weight:800;letter-spacing:.5px}
.projects-sub{left:0;top:770px;width:708px;text-align:center;color:var(--muted);font-size:7.1px;line-height:11px}
.filters{left:0;top:816px;width:708px;display:flex;justify-content:center;gap:10px;font-size:7.2px;font-weight:600;color:#333}
.filters .on{color:var(--purple)}

.grid{left:0;top:847px;width:708px;display:grid;grid-template-columns:repeat(4,1fr);grid-auto-rows:157px;gap:1px;background:#ddd}
.tile{position:relative}
.tile-label{position:absolute;left:0;bottom:19px;width:100%;text-align:center;color:var(--white);font-size:6.4px;font-weight:500;letter-spacing:.4px}
.t1{background:linear-gradient(135deg,#c9ccd2,#8a8d94 60%,#3d5d9a)}
.t2{background:linear-gradient(135deg,#3d8fb0,#d8e4ee 45%,#d14a6e 75%,#e89a4c)}
.t3{background:linear-gradient(135deg,#e8714e,#d9583a)}
.t4{background:linear-gradient(135deg,#6f7a2e,#b59a6a 50%,#d8d6cc)}
.t5{background:linear-gradient(180deg,#f2f2f2,#dedede 60%,#f7f7f7)}
.t6{background:linear-gradient(120deg,#2d3a6a,#5b6fa0 50%,#b9786a 80%,#e0a07a)}
.t7{background:linear-gradient(180deg,#151515,#555 60%,#9a9a9a)}
.t8{background:linear-gradient(180deg,#9fb0c8,#e8e8e8 45%,#6f8f55)}
</style>
</head>
<body>
<div class="page">

  <div class="abs topbar"></div>
  <div class="abs contact">
    <span>
      <svg width="6" height="6" viewBox="0 0 10 10"><path d="M2 0.5 L4 2.8 L3 4 Q4.5 6 6 7 L7.2 6 L9.5 8 L8 9.5 Q3 9 0.5 2 Z" fill="#fff"/></svg>
      08-555-0142
    </span>
    <span>
      <svg width="6" height="5" viewBox="0 0 12 9"><rect x=".7" y=".7" width="10.6" height="7.6" fill="none" stroke="#fff" stroke-width="1.3"/><path d="M.7 .7 L6 5 L11.3 .7" fill="none" stroke="#fff" stroke-width="1.3"/></svg>
      info@brightpage-web.co.il
    </span>
  </div>
  <svg class="abs tabs" width="240" height="22" viewBox="0 0 240 22">
    <polygon points="8,0 81,0 77,22 4,22" fill="var(--green)"/>
    <polygon points="81,0 157,0 153,22 77,22" fill="var(--purple)"/>
    <polygon points="157,0 240,0 240,22 153,22" fill="var(--yellow)"/>
  </svg>
  <div class="abs tab-label" style="left:497px">Get A Quote</div>
  <div class="abs tab-label" style="left:564px">Select Language</div>

  <div class="abs header"></div>
  <div class="abs brand"><i></i>BrightPage</div>
  <nav class="abs nav">
    <span class="active">HOME</span><span>ABOUT</span><span>PORTFOLIO</span><span>REVIEWS</span><span>SERVICES</span><span>LATEST BLOG</span><span>CONTACT</span>
  </nav>

  <div class="abs hero" role="img" aria-label="Person typing on a laptop at a wooden café table with a coffee mug"></div>
  <h1 class="abs hero-title">WE CREATE<br>THE WEB</h1>
  <p class="abs hero-sub">we craete professional website for you</p>
  <div class="abs hero-btn">GET A FREE QUOTE</div>

  <div class="abs ghost">WHO<br>ARE WE</div>
  <svg class="abs intro-shape" width="464" height="279" viewBox="0 0 464 279">
    <polygon points="0,0 394,0 463,278 0,278" fill="var(--purple)"/>
  </svg>
  <h2 class="abs intro-title">Are you looking for a PROFESSIONAL, EXPERIENCED, RELIABLE website company to create a successful online presence for your company?</h2>
  <p class="abs intro-text">For over 20 years, we have been designing, developing, marketing, maintaining and hosting custom-designed, content-driven, technically cutting-edge and easy-to-update sites while providing prompt, personal service.</p>
  <div class="abs intro-btn">GET A FREE QUOTE</div>

  <h2 class="abs projects-title">FEATURED PROJECTS</h2>
  <p class="abs projects-sub">We design and develop services for customers of all sizes, specializing in creating stylish,<br>modern websites, web services and online stores.</p>
  <div class="abs filters">
    <span class="on">SHOW ALL</span><span>WEB</span><span>ADV</span><span>BRANDING</span><span>DESIGN</span><span>PHOTO</span>
  </div>

  <div class="abs grid">
    <div class="tile t1" role="img" aria-label="Black and white portrait of an elderly woman beside a flag"></div>
    <div class="tile t2" role="img" aria-label="Scientist in a lab holding flasks of red liquid"></div>
    <div class="tile t3" role="img" aria-label="Hand writing with a pen under an orange overlay"><div class="tile-label">MERIDIAN GROUP INTERNATIONAL</div></div>
    <div class="tile t4" role="img" aria-label="Cupped hands catching running water"></div>
    <div class="tile t5" role="img" aria-label="Spoon of yogurt topped with a strawberry"></div>
    <div class="tile t6" role="img" aria-label="City skyline at dusk with rooftops"></div>
    <div class="tile t7" role="img" aria-label="Black and white city at night with light trails"></div>
    <div class="tile t8" role="img" aria-label="Industrial plant with white silos and gardens"></div>
  </div>

</div>
</body>
</html>
```